Summit Glossfloor & Honing
I'm looking for a business card and logo design for my
new Polished Concrete & Grinding business,
If you were to look up Summit in the dictionary it would
say, first in importance, order, or position; leading.
Polished Concrete floors are a niche market, that are being used currently in Shopping centres, office spaces and by most high end architects, builders and designers.
i need my business card & logo to stand out from my
competitors, i need my design + logo to reflect this it
needs to be simple, professional, eye catching, easy
to read and scream quality. The logo will need to be
suitable for a whole range of applications including,
uniforms, letter heads, stickers, and eventually
incorporating in vehicle vinyl wrapping.
Target Market(s)
Builders, architects, Interior designers & home owners
Contact Information for Business Card
Front side:
- Summit Glossfloor & Honing.
- Logo
Rear side:
- Liam Varga
- 0491735082
- info@summitgfh.com.au
- commercial - domestic - industrial
- (later down the line website & space for
social media links
www.summitglossfloor.com.au)
Colors
Designer to choose colors to be used in the design.
Look and feel

```html
<!DOCTYPE html>
<html lang="en">
<head>
<meta charset="utf-8">
<title>Summit Glossfloor &amp; Honing — Business Card</title>
<link rel="stylesheet" href="https://fonts.googleapis.com/css2?family=Roboto:wght@400;500;700&display=swap">
<style>
  :root {
    --backdrop: #1c1f22;
    --brand-blue: #22a6df;
    --brand-blue-light: #5cc5f0;
    --brand-blue-deep: #1a8cc4;
    --ink-dark: #231f20;
    --paper: #ffffff;
    --muted: #3a3a3a;
  }
  html, body {
    margin: 0;
    padding: 0;
    width: 1200px;
    height: 738px;
    overflow: hidden;
    background: var(--backdrop);
    font-family: "Roboto", Arial, sans-serif;
  }
  .canvas {
    position: relative;
    width: 1200px;
    height: 738px;
  }
  .card {
    position: absolute;
    top: 226px;
    width: 500px;
    height: 286px;
    overflow: hidden;
    box-shadow: 0 10px 30px rgba(0,0,0,0.5);
  }
  /* Front */
  .card-front {
    left: 60px;
    background: var(--brand-blue);
    color: var(--paper);
  }
  .front-name {
    position: absolute;
    top: 92px;
    left: 0;
    width: 100%;
    text-align: center;
    font-weight: 700;
    font-size: 30px;
    line-height: 1.2;
    letter-spacing: 0.5px;
    color: var(--paper);
  }
  .front-services {
    position: absolute;
    bottom: 30px;
    left: 0;
    width: 100%;
    text-align: center;
    font-weight: 400;
    font-size: 14px;
    letter-spacing: 1px;
  }
  /* Back */
  .card-back {
    left: 640px;
    background: var(--paper);
  }
  .back-wave {
    position: absolute;
    inset: 0;
  }
  .holder {
    position: absolute;
    top: 20px;
    right: 26px;
    text-align: right;
  }
  .holder-name {
    font-weight: 500;
    font-size: 21px;
    letter-spacing: 2px;
    color: var(--brand-blue);
    text-transform: uppercase;
  }
  .holder-role {
    font-size: 10px;
    color: var(--muted);
    margin-top: 1px;
  }
  .back-name {
    position: absolute;
    top: 92px;
    left: 22px;
    width: 240px;
    font-weight: 700;
    font-size: 24px;
    line-height: 1.2;
    color: var(--brand-blue);
  }
  .contact {
    position: absolute;
    right: 20px;
    bottom: 40px;
    list-style: none;
    margin: 0;
    padding: 0;
    text-align: right;
    color: var(--paper);
    font-size: 13px;
    line-height: 20px;
  }
  .contact li {
    display: flex;
    justify-content: flex-end;
    align-items: center;
    gap: 8px;
  }
  .contact svg {
    width: 10px;
    height: 10px;
    fill: none;
    stroke: var(--brand-blue);
    stroke-width: 1.6;
  }
</style>
</head>
<body>
<div class="canvas">

  <section class="card card-front">
    <div class="front-name">Summit Glossfloor<br>&amp; Honing</div>
    <div class="front-services">COMMERCIAL - DOMESTIC - INDUSTRIAL</div>
  </section>

  <section class="card card-back">
    <svg class="back-wave" viewBox="0 0 500 286" preserveAspectRatio="none" aria-hidden="true">
      <path d="M0,232 C130,268 260,246 340,176 C400,124 450,108 500,102 L500,286 L0,286 Z" fill="var(--ink-dark)"/>
      <path d="M0,214 C140,256 270,236 345,164 C400,114 450,98 500,92" fill="none" stroke="var(--brand-blue)" stroke-width="7"/>
      <path d="M0,222 C150,262 280,244 352,172 C405,124 452,104 500,100" fill="none" stroke="var(--brand-blue-light)" stroke-width="4"/>
    </svg>

    <div class="holder">
      <div class="holder-name">Liam Varga</div>
      <div class="holder-role">Director</div>
    </div>

    <div class="back-name">Summit Glossfloor<br>&amp; Honing</div>

    <ul class="contact">
      <li>0491735082
        <svg viewBox="0 0 10 10"><path d="M2,1 L4,3 L3,4 C4,6 5,7 6,7 L7,6 L9,8 L8,9 C4,9 1,6 1,2 Z"/></svg>
      </li>
      <li>info@summitgfh.com.au
        <svg viewBox="0 0 10 10"><rect x="1" y="2" width="8" height="6"/><path d="M1,2 L5,5.5 L9,2"/></svg>
      </li>
      <li>www.summitglossfloor.com.au
        <svg viewBox="0 0 10 10"><circle cx="5" cy="5" r="4"/><path d="M1,5 H9 M5,1 C3,3.5 3,6.5 5,9 M5,1 C7,3.5 7,6.5 5,9"/></svg>
      </li>
    </ul>
  </section>

</div>
</body>
</html>
```